The most modern business card ever !!!

Our company call “Vantilo”. Vantilo is a technology company specialized in cruises solutions. Out main product is a platform to reserve cruises. This is a revolutionary platform that make easier to travel agencies and final users to reserve cruises across dozen companies like tarvik, welbi, dpv, hbt, etc..We are a “start up”, with a young team of developers and we want to transmit it.. For it, we want something different, a modern business card that represent cruises and technology.. When someone receive this card, this person should say: wowww this is different… this is modern… this is a cruise related company..
Contact Information for Business Card
Requirements
Must have
- diferent, modern
Should not have
- traditions business card

```html
<!DOCTYPE html>
<html lang="en">
<head>
<meta charset="utf-8">
<title>Vantilo Business Card</title>
<link href="https://fonts.googleapis.com/css2?family=Oswald:wght@400;600&display=swap" rel="stylesheet">
<style>
  :root {
    --page-bg: #9a6a4c;
    --card-top: #e9cfc2;
    --card-mid: #f3d6c9;
    --card-bottom: #e2c6b3;
    --card-edge: rgba(255, 255, 255, 0.85);
    --accent-blue: #29abe2;
    --ink: #111111;
  }
  * { margin: 0; padding: 0; box-sizing: border-box; }
  html, body {
    width: 1200px;
    height: 970px;
    overflow: hidden;
  }
  body {
    background: var(--page-bg);
    position: relative;
    font-family: "Oswald", "Arial Narrow", sans-serif;
    color: var(--ink);
  }
  .business-card {
    position: absolute;
    left: 360px;
    top: 51px;
    width: 475px;
    height: 831px;
    border-radius: 16px;
    border: 1px solid var(--card-edge);
    background: linear-gradient(170deg, var(--card-top) 0%, var(--card-mid) 45%, var(--card-bottom) 100%);
    overflow: hidden;
  }
  .accent-arrow {
    position: absolute;
    inset: 0;
    width: 475px;
    height: 831px;
  }
  .brand-name {
    position: absolute;
    left: 110px;
    top: 380px;
    font-family: "Oswald", "Arial Narrow", sans-serif;
    font-weight: 600;
    font-size: 70px;
    line-height: 1;
    letter-spacing: 18px;
    color: var(--ink);
    white-space: nowrap;
  }
  .contact-block {
    position: absolute;
    left: 31px;
    top: 688px;
  }
  .person-name {
    font-weight: 600;
    font-size: 27px;
    line-height: 1;
    text-transform: uppercase;
  }
  .person-role {
    font-weight: 400;
    font-size: 21px;
    line-height: 1.1;
    margin-top: 1px;
  }
  .contact-lines {
    margin-top: 12px;
    font-weight: 400;
    font-size: 21px;
    line-height: 26px;
    white-space: nowrap;
  }
</style>
</head>
<body>
  <div class="business-card">
    <svg class="accent-arrow" viewBox="0 0 475 831" aria-hidden="true">
      <polygon points="475,77 475,765 157,421" fill="var(--accent-blue)"/>
    </svg>
    <div class="brand-name">Vantilo</div>
    <div class="contact-block">
      <div class="person-name">Elias Marren</div>
      <div class="person-role">Owner/President</div>
      <div class="contact-lines">
        <div>P: 555-204-7713 | E: info@vantilocruise.com</div>
        <div>W: www.vantilocruise.com</div>
      </div>
    </div>
  </div>
</body>
</html>
```